RB Promotions a premium promotional agency needs design of business cards

I'm looking for a premium classy business card - possibly the Logo (the two backward R's) to be raised. Black and white for colour scheme would be preferable. I have attached my initial idea but open to your suggestions. We are a promotional agency who promote high profile brands. Thank you.

Contact Information for Business Card

MARLA WHITCOMBE
+64 21 555 0193
Marla@RBpromoagency.net
www.RBpromoagency.net

Colors
000000
ffffff

```html
<!DOCTYPE html>
<html lang="en">
<head>
<meta charset="utf-8">
<title>RB Promotions – Business Card</title>
<link href="https://fonts.googleapis.com/css2?family=Marcellus&family=EB+Garamond:wght@400;700&display=swap" rel="stylesheet">
<style>
  :root {
    --page-bg: #d9dadc;
    --card-black: #000000;
    --card-mid: #1b1b1c;
    --card-edge: #0a0a0a;
    --ink-white: #ffffff;
    --ink-soft: #e6e6e6;
    --rule: rgba(255, 255, 255, 0.55);
  }
  * { margin: 0; padding: 0; box-sizing: border-box; }
  html, body {
    width: 1200px;
    height: 1200px;
    overflow: hidden;
    background: var(--page-bg);
  }
  .canvas {
    position: relative;
    width: 1200px;
    height: 1200px;
  }
  .card {
    position: absolute;
    left: 167px;
    width: 839px;
    height: 474px;
    background:
      radial-gradient(ellipse 70% 45% at 50% 42%, var(--card-mid) 0%, var(--card-edge) 70%, var(--card-black) 100%);
    overflow: hidden;
  }
  .card--front { top: 96px; }
  .card--back { top: 600px; height: 477px; }

  .wordmark {
    position: absolute;
    left: 0;
    right: 0;
    top: 192px;
    text-align: center;
    font-family: "Marcellus", serif;
    font-weight: 400;
    font-size: 92px;
    line-height: 1;
    color: var(--ink-white);
  }

  .brand-block {
    position: absolute;
    left: 0;
    width: 325px;
    top: 0;
    bottom: 0;
    display: flex;
    align-items: center;
    justify-content: center;
  }
  .brand-name {
    font-family: "Marcellus", serif;
    font-size: 34px;
    color: var(--ink-white);
    line-height: 1;
    margin-top: 20px;
  }

  .divider {
    position: absolute;
    left: 325px;
    top: 40px;
    width: 2px;
    height: 360px;
    background: linear-gradient(to bottom, transparent 0%, var(--rule) 25%, var(--rule) 75%, transparent 100%);
  }

  .contact {
    position: absolute;
    left: 391px;
    top: 136px;
    font-family: "EB Garamond", serif;
    color: var(--ink-soft);
  }
  .contact__name {
    font-weight: 700;
    font-size: 29px;
    letter-spacing: 0.5px;
    color: var(--ink-white);
    line-height: 1;
    margin-bottom: 24px;
  }
  .contact__line {
    font-size: 25px;
    line-height: 1;
    margin-bottom: 22px;
  }
  .contact__line--web { margin-top: 4px; }
</style>
</head>
<body>
  <main class="canvas">
    <section class="card card--front" aria-label="Card front">
      <div class="wordmark">RB Promotions</div>
    </section>

    <section class="card card--back" aria-label="Card back">
      <div class="brand-block">
        <span class="brand-name">RB Promotions</span>
      </div>
      <div class="divider"></div>
      <div class="contact">
        <p class="contact__name">MARLA WHITCOMBE</p>
        <p class="contact__line">+64 21 555 0193</p>
        <p class="contact__line">Marla@RBpromoagency.net</p>
        <p class="contact__line contact__line--web">www.RBpromoagency.net</p>
      </div>
    </section>
  </main>
</body>
</html>
```